Cedarline Residences —-

Letter head for my apartment building of 15 Floors
In Kampala, Uganda

CEDARLINE RESIDENCIES
14 KIVARA RIDGE ROAD
NAGURU - KAMPALA
P.O. BOX 38516
KAMPALA— UGANDA

```html
<!DOCTYPE html>
<html lang="en">
<head>
<meta charset="utf-8">
<title>Cedarline Residences — Letterhead</title>
<link rel="stylesheet" href="https://fonts.googleapis.com/css2?family=Open+Sans:wght@400;600;700&display=swap">
<style>
  :root {
    --backdrop: #ececec;
    --paper: #fbfbfb;
    --brand-blue: #1f6fbd;
    --band-grey: #8e92a6;
    --ink: #4a4a4a;
    --ink-soft: #5c5c5c;
    --signature-tone: #e6e6e8;
  }
  * { box-sizing: border-box; margin: 0; padding: 0; }
  html, body {
    width: 1200px; height: 795px; overflow: hidden;
    background: var(--backdrop);
    font-family: "Open Sans", sans-serif;
  }
  .canvas {
    position: relative; width: 1200px; height: 795px;
    display: flex; align-items: center; justify-content: center;
  }
  .letterhead {
    position: relative;
    width: 534px; height: 755px;
    background: var(--paper);
    box-shadow: 0 4px 18px rgba(0,0,0,0.10);
    color: var(--ink);
  }
  .brand-name {
    position: absolute; left: 48px; top: 116px;
    font-size: 17px; font-weight: 700; letter-spacing: 0.5px;
    color: var(--brand-blue);
  }
  .contact-list {
    position: absolute; right: 48px; top: 48px;
    list-style: none; font-size: 8.5px; line-height: 12px; color: var(--ink-soft);
  }
  .contact-list li { display: flex; align-items: center; gap: 4px; }
  .contact-list svg { width: 8px; height: 8px; fill: var(--brand-blue); flex: none; }
  .letter-body {
    position: absolute; left: 78px; top: 190px; width: 382px;
    font-size: 9px; line-height: 13.2px; color: var(--ink);
  }
  .salutation { margin-bottom: 12px; }
  .letter-body p.paragraph { margin-bottom: 14px; }
  .closing { margin-top: 4px; }
  .signature-area {
    width: 74px; height: 46px; margin: 12px 0 0 28px;
    background: var(--signature-tone); border-radius: 4px;
  }
  .footer-address {
    position: absolute; left: 82px; right: 48px; bottom: 22px;
    display: flex; align-items: center; gap: 5px;
    font-size: 10px; color: var(--ink);
  }
  .footer-address svg { width: 9px; height: 11px; fill: var(--brand-blue); flex: none; }
  .footer-band {
    position: absolute; left: 0; right: 0; bottom: 0; height: 7px; display: flex;
  }
  .footer-band .band-blue { width: 48%; background: var(--brand-blue); }
  .footer-band .band-grey { flex: 1; background: var(--band-grey); margin-top: 3px; }
</style>
</head>
<body>
<main class="canvas">
  <article class="letterhead">
    <header>
      <div class="brand-name">CEDARLINE RESIDENCES</div>
      <ul class="contact-list">
        <li>
          <svg viewBox="0 0 10 10"><path d="M2 1l2 2-1 1.3c.6 1.2 1.5 2.1 2.7 2.7L7 6l2 2-1.2 1.2C4.5 9 1 5.5.8 2.2z"/></svg>
          949.482.5170
        </li>
        <li>
          <svg viewBox="0 0 10 10"><path d="M0 2h10v6H0zM.6 2.4L5 5.6l4.4-3.2" /><path d="M.8 2.6L5 5.4l4.2-2.8V7.4H.8z" fill="#fff"/></svg>
          hello@cedarline-res.com
        </li>
        <li>
          <svg viewBox="0 0 10 10"><circle cx="5" cy="5" r="4.6"/></svg>
          www.cedarline-res.com
        </li>
      </ul>
    </header>

    <section class="letter-body">
      <p class="salutation">Dear customer,</p>
      <p class="paragraph">Lorem ipsum dolor sit amet, consectetur adipisicing elit, sed do eiusmod tempor incididunt ut labore et dolore magna aliqua. Ut enim ad minim veniam, quis nostrud exercitation ullamco laboris nisi ut aliquip ex ea commodo consequat. Duis aute irure dolor in reprehenderit in voluptate velit esse cillum dolore eu fugiat nulla pariatur. Excepteur sint occaecat cupidatat non proident, sunt in culpa qui officia deserunt mollit anim id est laborum.</p>
      <p class="paragraph">Lorem ipsum dolor sit amet, consectetur adipisicing elit, sed do eiusmod tempor incididunt ut labore et dolore magna aliqua. Ut enim ad minim veniam, quis nostrud exercitation ullamco laboris nisi ut aliquip ex ea commodo consequat. Duis aute irure dolor in reprehenderit in voluptate velit esse cillum dolore eu fugiat nulla pariatur. Excepteur sint occaecat cupidatat non proident, sunt in culpa qui officia deserunt mollit anim id est laborum.</p>
      <p class="paragraph">Lorem ipsum dolor sit amet, consectetur adipisicing elit, sed do eiusmod tempor incididunt ut labore et dolore magna aliqua. Ut enim ad minim veniam, quis nostrud exercitation ullamco laboris nisi ut aliquip ex ea commodo consequat. Duis aute irure dolor in reprehenderit in voluptate velit esse cillum dolore eu fugiat nulla pariatur. Excepteur sint occaecat cupidatat non proident, sunt in culpa qui officia deserunt mollit anim id est laborum.</p>
      <p class="paragraph">Lorem ipsum dolor sit amet, consectetur adipisicing elit, sed do eiusmod tempor incididunt ut labore et dolore magna aliqua. Ut enim ad minim veniam, quis nostrud exercitation ullamco laboris nisi ut aliquip ex ea commodo consequat. Duis aute irure dolor in reprehenderit.</p>
      <p class="closing">Yours Sincerely,</p>
      <div class="signature-area" role="img" aria-label="Handwritten signature of the sender"></div>
    </section>

    <footer>
      <div class="footer-address">
        <svg viewBox="0 0 10 12"><path d="M5 0a4 4 0 0 1 4 4c0 3-4 8-4 8S1 7 1 4a4 4 0 0 1 4-4zm0 2.4A1.6 1.6 0 1 0 5 5.6 1.6 1.6 0 0 0 5 2.4z"/></svg>
        14 Kivara Ridge Road Naguru - Kampala P.O. Box 38516 Kampala — Uganda
      </div>
      <div class="footer-band">
        <span class="band-blue"></span>
        <span class="band-grey"></span>
      </div>
    </footer>
  </article>
</main>
</body>
</html>
```